Ferrowave.com website design

I need a basic website for www.ferrowave.com. Ferro Wave has been hosting websites since 2002 via partnership arrangement with Stackhollow.com and Namequarry.com. We do not do any design, only hosting for small companies and nonprofits. We are referring people to PixelGuild and others to get their websites developed. Our website and pricing does not change often, but I need to be able to easily update the pricing and contact page.

Target Market(s)

Small company and non profit organizations

Industry/Entity Type

Utility

Coding

Coded - Design and coding required

Number of Pages Required

5+ page

Colors

Designer to choose colors to be used in the design.

Requirements
Must have
• Wordsmith format for easy content management. The logo attached. Contact us page with the following: Phone and fax are the same number: 888.514.2973. Email address is myferrowave@mailnest.example. Mailing address is 4819 E. Tolliver Bend #317, Searcy, AR 72143.
Nice to have
• Some kind of badge or tag line on the home page that celebrates our 15th year of hosting without a single hosting without any downtime. We are are 15 year partners with Stackhollow.com and Namequarry.com. Website Design tab needs to reference PixelGuild or others for all their website design needs. We provide no design or updating services. We will provide the developers FTP access to our dedicated Linux server. We do not provide email services other than redirects to their proprietary email or gmail, yahoo, etc. Needs a services and pricing tab. We provide domain registration services via our partnership with Namequarry.com. We will want a way for them to submit a suggested domain name for us to verify if available. I might be able to get a link from Namequarry.com to our account for you to include on that tab REGISTER DOMAIN. The tab buttons can be: WHO WE ARE, WHAT WE DO, WHEN YOU NEED US, WHERE TO REACH US. Maybe consider making the WHO, WHAT, WHEN and WHERE a dark blue color the rest of the text different color just so they stand out
Should not have
• A lot of animation that takes a long time to open. Clean and simple website.

```html
<!DOCTYPE html>
<html lang="en">
<head>
<meta charset="utf-8">
<title>Ferro Wave – Web Hosting</title>
<link rel="stylesheet" href="https://fonts.googleapis.com/css2?family=Montserrat:wght@400;600;700;800&family=Open+Sans:wght@400;600;700&display=swap">
<style>
:root{
  --blue:#2f80c6;
  --blue-deep:#1f5f9c;
  --navy:#173a5e;
  --ink:#2b3440;
  --muted:#7c8794;
  --dark:#1d2530;
  --paper:#ffffff;
  --soft:#f2f4f6;
  --footer-bar:#16202b;
}
*{box-sizing:border-box;margin:0;padding:0}
html,body{width:771px;height:1200px;overflow:hidden}
body{font-family:"Open Sans",Arial,sans-serif;color:var(--ink);background:var(--paper);position:relative}
.hero{position:absolute;left:0;top:0;width:771px;height:342px;
  background:linear-gradient(160deg,#3d4a57 0%,#2a3440 45%,#4d5866 75%,#252d37 100%)}
.hero-photo{position:absolute;inset:0}
.topbar{position:absolute;top:6px;right:60px;display:flex;gap:14px;font-size:7px;font-weight:700;color:#fff;letter-spacing:.5px}
.topbar span.search{border-bottom:1px solid rgba(255,255,255,.6);padding-right:30px}
.header{position:absolute;left:56px;top:20px;width:660px;height:50px;background:var(--paper);display:flex;align-items:center;justify-content:space-between;padding:0 14px}
.brand{display:flex;align-items:center;gap:8px}
.brand-square{width:26px;height:26px;background:var(--blue)}
.brand-name{font-family:"Montserrat",sans-serif;font-weight:800;font-size:15px;color:var(--navy);letter-spacing:.5px;line-height:1}
.brand-tag{font-size:5.5px;color:var(--muted);letter-spacing:1.5px;margin-top:3px}
.nav{display:flex;gap:16px;font-family:"Montserrat",sans-serif;font-size:7.5px;font-weight:700;color:var(--muted)}
.nav b{color:var(--navy)}
.badge{position:absolute;left:283px;top:112px;width:205px;height:212px}
.badge-text{position:absolute;inset:0;display:flex;flex-direction:column;align-items:center;justify-content:center;color:#fff;font-family:"Montserrat",sans-serif;text-align:center}
.badge-small{font-size:8.5px;font-weight:700;letter-spacing:1.5px;line-height:1.3}
.badge-big{font-size:38px;font-weight:800;line-height:1;margin:6px 0 2px;border-top:1px solid #fff;border-bottom:1px solid #fff;padding:3px 4px}
.badge-mid{font-size:9px;font-weight:700;letter-spacing:3px;margin-bottom:8px}
.domain-bar{position:absolute;left:0;top:342px;width:771px;height:62px;background:var(--blue);display:flex;align-items:center;padding:0 58px;color:#fff}
.domain-title{font-family:"Montserrat",sans-serif;font-size:14px;font-weight:700;letter-spacing:.5px}
.domain-sub{font-size:7px;opacity:.85;margin-top:2px}
.domain-form{margin-left:auto;display:flex;gap:8px}
.domain-input{width:200px;height:22px;background:var(--blue-deep);font-size:7px;color:rgba(255,255,255,.75);padding:6px 10px}
.domain-submit{width:50px;height:22px;background:var(--paper);color:var(--blue);font-size:7px;font-weight:700;display:flex;align-items:center;justify-content:center}
.services{position:absolute;left:0;top:404px;width:771px;height:350px;background:var(--soft)}
.section-title{font-family:"Montserrat",sans-serif;font-size:18px;font-weight:700;color:var(--ink);letter-spacing:.5px}
.section-title em{font-style:normal;color:var(--blue)}
.services .section-title{position:absolute;top:30px;width:100%;text-align:center}
.title-rule{width:34px;height:2px;background:var(--blue);margin:6px auto 0}
.service-list{position:absolute;top:100px;left:128px;width:515px;display:flex;justify-content:space-between}
.service{width:145px;text-align:center}
.service svg{display:block;margin:0 auto 8px}
.service-name{font-family:"Montserrat",sans-serif;font-size:7.5px;font-weight:700;color:var(--blue);line-height:1.35;min-height:22px}
.service-price{font-family:"Montserrat",sans-serif;font-size:28px;font-weight:400;color:var(--ink);margin:4px 0 4px}
.service-text{font-size:6.5px;color:var(--muted);line-height:1.45;height:30px}
.btn{display:inline-block;background:var(--dark);color:#fff;font-family:"Montserrat",sans-serif;font-size:6.5px;font-weight:700;padding:7px 12px;letter-spacing:.5px;margin-top:12px}
.about{position:absolute;left:0;top:754px;width:771px;height:244px;background:var(--paper)}
.about-photo{position:absolute;left:56px;top:40px;width:316px;height:168px;background:linear-gradient(135deg,#dfe6ec,#b9c7d3 55%,#8ea2b4)}
.about-copy{position:absolute;left:392px;top:46px;width:325px}
.about-copy .section-title{font-size:17px}
.about-copy .title-rule{margin:6px 0 10px}
.about-text{font-size:6.8px;color:var(--muted);line-height:1.6}
.about-copy .btn{margin-top:12px}
.footer{position:absolute;left:0;top:998px;width:771px;height:174px;background:var(--blue);color:#fff;display:flex;padding:22px 58px 0}
.footer-col{width:200px}
.footer-col h4{font-family:"Montserrat",sans-serif;font-size:9px;font-weight:700;letter-spacing:.5px;margin-bottom:8px}
.footer-col li{list-style:none;font-size:6.5px;line-height:1.75}
.social{display:flex;gap:6px;margin-top:8px}
.social span{width:10px;height:10px;border-radius:50%;background:#fff}
.contact dt{font-size:6px;font-weight:700;letter-spacing:.4px;margin-top:5px}
.contact dd{font-size:6.5px;line-height:1.4}
.partners h4{font-size:13px}
.partner{width:78px;height:22px;background:var(--paper);border-radius:3px;margin-bottom:8px}
.partner.dark{background:var(--dark)}
.legal{position:absolute;left:0;top:1172px;width:771px;height:28px;background:var(--footer-bar);color:#c6ced7;font-size:6px;display:flex;align-items:center;justify-content:space-between;padding:0 58px}
</style>
</head>
<body>
<section class="hero">
  <div class="hero-photo" role="img" aria-label="Dimmed photograph of a laptop and notebooks on a desk"></div>
  <div class="topbar"><span>LOGIN</span><span>|</span><span>REGISTER</span><span class="search">SEARCH</span></div>
  <header class="header">
    <div class="brand">
      <span class="brand-square"></span>
      <div><div class="brand-name">FERRO WAVE</div><div class="brand-tag">WEB HOSTING SINCE 2002</div></div>
    </div>
    <nav class="nav"><span><b>WHO</b> WE ARE</span><span><b>WHAT</b> WE DO</span><span><b>WHEN</b> YOU NEED US</span><span><b>WHERE</b> TO REACH US</span></nav>
  </header>
  <div class="badge">
    <svg width="205" height="212" viewBox="0 0 205 212">
      <polygon points="102.5,4 199,56 199,156 102.5,208 6,156 6,56" fill="rgba(30,40,52,.55)" stroke="#fff" stroke-width="3"/>
    </svg>
    <div class="badge-text">
      <div class="badge-small">CELEBRATE OUR</div>
      <div class="badge-big">15 YEARS</div>
      <div class="badge-mid">OF HOSTING</div>
      <div class="badge-small">WITHOUT ANY<br>DOWNTIME</div>
    </div>
  </div>
</section>

<section class="domain-bar">
  <div>
    <div class="domain-title">SUGGEST A DOMAIN NAME</div>
    <div class="domain-sub">Tell us the name you want and we check it for you.</div>
  </div>
  <div class="domain-form">
    <div class="domain-input">Enter your domain name</div>
    <div class="domain-submit">SUBMIT</div>
  </div>
</section>

<section class="services">
  <h2 class="section-title">OUR <em>SERVICES</em><div class="title-rule"></div></h2>
  <div class="service-list">
    <div class="service">
      <svg width="30" height="28" viewBox="0 0 30 28" fill="none" stroke="#2b3440" stroke-width="1.6"><path d="M8 20H6a5 5 0 0 1 0-10 7 7 0 0 1 13-2 5.5 5.5 0 0 1 5 12h-2"/><path d="M15 26V14M11 18l4-4 4 4"/></svg>
      <div class="service-name">WEB HOSTING</div>
      <div class="service-price">$9.99</div>
      <div class="service-text">Reliable hosting on our dedicated Linux server for small companies and nonprofits, with no downtime.</div>
      <span class="btn">READ MORE</span>
    </div>
    <div class="service">
      <svg width="30" height="28" viewBox="0 0 30 28" fill="none" stroke="#2b3440" stroke-width="1.6"><circle cx="15" cy="14" r="11"/><path d="M4 14h22M15 3c4 4 4 18 0 22M15 3c-4 4-4 18 0 22"/></svg>
      <div class="service-name">DOMAIN REGISTRATION<br>SERVICES</div>
      <div class="service-price">$9.99</div>
      <div class="service-text">Register your domain through our trusted partner and let us check that your name is free.</div>
      <span class="btn">READ MORE</span>
    </div>
    <div class="service">
      <svg width="30" height="28" viewBox="0 0 30 28" fill="none" stroke="#2b3440" stroke-width="1.6"><rect x="3" y="3" width="20" height="14"/><path d="M16 12v12M16 12l8 7-4 .5 2 4"/></svg>
      <div class="service-name">WEBSITE DEVELOPMENT<br>SOLUTIONS</div>
      <div class="service-price">$9.99</div>
      <div class="service-text">We refer you to skilled developers and give them FTP access to build your site.</div>
      <span class="btn">READ MORE</span>
    </div>
  </div>
</section>

<section class="about">
  <div class="about-photo" role="img" aria-label="Photograph of hands using a tablet beside a laptop"></div>
  <div class="about-copy">
    <h2 class="section-title">ABOUT <em>FERRO WAVE</em></h2>
    <div class="title-rule"></div>
    <p class="about-text">Ferro Wave has hosted websites for small companies and nonprofit groups since 2002. We focus on one thing only: keeping your site online. Through long partnerships we offer domain registration and dependable hosting on a dedicated Linux server. For design and updates we refer you to trusted developers, and we give them the access they need to get the job done.</p>
    <span class="btn">READ MORE</span>
  </div>
</section>

<footer class="footer">
  <div class="footer-col">
    <h4>SITEMAP</h4>
    <ul><li>Home</li><li>Who We Are</li><li>What We Do</li><li>When You Need Us</li><li>Where To Reach Us</li></ul>
    <div class="social"><span></span><span></span><span></span></div>
  </div>
  <div class="footer-col contact">
    <h4>CONTACT DETAILS</h4>
    <dl>
      <dt>PHONE &amp; FAX</dt><dd>888.514.2973</dd>
      <dt>EMAIL ADDRESS</dt><dd>myferrowave@mailnest.example</dd>
      <dt>ADDRESS</dt><dd>4819 E. Tolliver Bend #317<br>Searcy, AR 72143</dd>
    </dl>
  </div>
  <div class="footer-col partners">
    <h4>OUR PARTNERS</h4>
    <div class="partner"></div>
    <div class="partner dark"></div>
  </div>
</footer>

<div class="legal"><span>Privacy Policy &nbsp;|&nbsp; Terms of Use</span><span>Copyright 2017 Ferro Wave. All Rights Reserved.</span></div>
</body>
</html>
```